Business Folder

I need a fresh, modern design for a business folder. I have our company's colors, logo, and a separate file for just the graphic part of our logo as a design element. No photo, just colors, gradients, and shadows to create depth. I like the idea of a rich grey as the background, however, I realize we'd have to lighten to 'Tax Advisory Services' part of our logo.

The design would just be the 'front' or outside of the folder from Zelvora. Design file attached. You can find that here under 9 x 12 standard folder, Left and Right Pockets With Slit Both Sides:

https://www.zelvora-example.com/content.html?id=folderDownloadTemplates&rightMenuId=rightMenu&footerId=bodyFooterStyle6

```html
<!DOCTYPE html>
<html lang="en">
<head>
<meta charset="utf-8">
<title>Corvana Tax Advisory Services – Presentation Folder</title>
<link rel="stylesheet" href="https://fonts.googleapis.com/css2?family=Lato:wght@400;700;900&display=swap">
<style>
  :root {
    --stage: #3a3a3c;
    --paper: #ffffff;
    --navy: #0b4f82;
    --slate: #3f6690;
    --blue: #1c95d2;
    --sky: #6fc7e3;
    --cyan: #4dc6e8;
    --dieline: #000000;
  }
  html, body {
    margin: 0;
    padding: 0;
    width: 1200px;
    height: 1200px;
    overflow: hidden;
    background: var(--stage);
  }
  .folder-spread {
    display: block;
    width: 1200px;
    height: 1200px;
  }
  .brand-name {
    font-family: "Lato", sans-serif;
    font-weight: 900;
    fill: var(--navy);
  }
  .brand-tagline {
    font-family: "Lato", sans-serif;
    font-weight: 400;
    fill: var(--navy);
    letter-spacing: 2.2px;
  }
  .contact-heading,
  .contact-line {
    font-family: "Lato", sans-serif;
    font-weight: 400;
    fill: var(--paper);
  }
</style>
</head>
<body>
<svg class="folder-spread" viewBox="0 0 1500 1500" xmlns="http://www.w3.org/2000/svg" aria-label="Corvana folder outside spread">
  <defs>
    <linearGradient id="top-band-tone" x1="0" y1="0" x2="1" y2="0">
      <stop offset="0" stop-color="var(--navy)"/>
      <stop offset="0.3" stop-color="var(--slate)"/>
      <stop offset="0.5" stop-color="var(--sky)"/>
      <stop offset="0.7" stop-color="var(--slate)"/>
      <stop offset="1" stop-color="var(--navy)"/>
    </linearGradient>
    <linearGradient id="top-band-fade" x1="0" y1="0" x2="0" y2="1">
      <stop offset="0" stop-color="#ffffff" stop-opacity="0"/>
      <stop offset="0.55" stop-color="#ffffff" stop-opacity="0"/>
      <stop offset="1" stop-color="#ffffff" stop-opacity="1"/>
    </linearGradient>
    <linearGradient id="bottom-band-tone" x1="0" y1="0" x2="0" y2="1">
      <stop offset="0" stop-color="#ffffff"/>
      <stop offset="0.3" stop-color="var(--blue)"/>
      <stop offset="0.55" stop-color="var(--navy)"/>
      <stop offset="1" stop-color="var(--navy)"/>
    </linearGradient>
    <path id="pocket-tab" d="M91,1042 L36,1060 L36,1318 L91,1335" fill="none" stroke="var(--dieline)" stroke-width="2"/>
  </defs>

  <rect class="cover-panel" x="91" y="165" width="1318" height="876" fill="var(--paper)"/>

  <g class="top-artwork" role="img" aria-label="Decorative layered blue geometric band across the top of the cover">
    <rect x="91" y="165" width="1318" height="315" fill="url(#top-band-tone)"/>
    <rect x="91" y="165" width="1318" height="315" fill="url(#top-band-fade)"/>
  </g>

  <g class="bottom-artwork" role="img" aria-label="Decorative layered blue geometric band along the bottom of the cover">
    <rect x="91" y="810" width="1318" height="231" fill="url(#bottom-band-tone)"/>
  </g>

  <g class="brand-block">
    <text class="brand-name" x="1289" y="628" font-size="92" text-anchor="end">Corvana</text>
    <text class="brand-tagline" x="1289" y="655" font-size="21" text-anchor="end">TAX ADVISORY SERVICES</text>
  </g>

  <g class="contact-block" text-anchor="end">
    <text class="contact-heading" x="695" y="933" font-size="17">Address:</text>
    <text class="contact-line" x="695" y="953" font-size="13.5">Lorem ipsum dolor sit amet,</text>
    <text class="contact-line" x="695" y="970" font-size="13.5">consectetuer adipiscing elit, sed diam</text>
    <text class="contact-line" x="695" y="987" font-size="13.5">nonummy nibh</text>
    <text class="contact-line" x="695" y="1003" font-size="13.5">Ph: 0000 000 000, Fax: 0000 000 000</text>
  </g>

  <line class="pocket-fold" x1="91" y1="1041" x2="1409" y2="1041" stroke="var(--paper)" stroke-width="2"/>

  <g class="pockets">
    <polygon class="pocket-left" fill="var(--cyan)" points="91,1042 747,1042 723,1335 91,1335"/>
    <polygon class="pocket-right" fill="var(--cyan)" points="755,1042 1409,1042 1409,1335 777,1335"/>
    <use href="#pocket-tab"/>
    <use href="#pocket-tab" transform="translate(1500,0) scale(-1,1)"/>
  </g>
</svg>
</body>
</html>
```